Medical supplies company needs a catalogue re-design

Our present catalogue is spread over a number of pages but this needs to be reduced. 4-5 images would require to be on each page. It needs to be professional, simple and elegant. The photos and descriptors need to be adjacent to each other. It should be able to be emailed conventionally as an e-catalogue without it being compressed. an email with existing catalogue will be emailed to anyone interested.
https://www.quillvault.net/s/81tazup7rqwmdlon/consumables%20photos%20and%20descriptions.pdf?dl=0
Target Market(s)
medical practices, hospitals
Industry/Entity Type
Medical Supply

```html
<!DOCTYPE html>
<html lang="en">
<head>
<meta charset="UTF-8">
<title>Orvena Care — 2018 Winter Catalogue</title>
<link href="https://fonts.googleapis.com/css2?family=Montserrat:wght@400;600;700;800&display=swap" rel="stylesheet">
<style>
  :root {
    --brand-red: #e1232d;
    --brand-red-light: #e9474e;
    --brand-red-dark: #c41b25;
    --wall-light: #f4f2ee;
    --wall-warm: #e9e3d8;
    --floor-tone: #cfc3b2;
    --white: #ffffff;
  }
  * { margin: 0; padding: 0; box-sizing: border-box; }
  html, body {
    width: 1200px;
    height: 927px;
    overflow: hidden;
    background: var(--white);
  }
  .catalogue-cover {
    position: relative;
    width: 1200px;
    height: 927px;
    overflow: hidden;
    font-family: "Montserrat", sans-serif;
  }
  .cover-photo {
    position: absolute;
    inset: 0;
    background:
      linear-gradient(90deg, var(--wall-light) 0%, var(--wall-light) 32%, var(--wall-warm) 48%, #f6f3ee 62%, var(--wall-light) 100%),
      var(--wall-light);
  }
  .cover-photo::after {
    content: "";
    position: absolute;
    left: 0; right: 0; bottom: 0;
    height: 120px;
    background: linear-gradient(180deg, rgba(207,195,178,0) 0%, var(--floor-tone) 100%);
    opacity: 0.5;
  }
  .cover-shapes {
    position: absolute;
    inset: 0;
  }
  .brand-name {
    position: absolute;
    left: 68px;
    top: 230px;
    display: flex;
    align-items: center;
    gap: 14px;
    color: var(--brand-red);
    font-weight: 700;
  }
  .brand-name__dot {
    width: 22px;
    height: 22px;
    border-radius: 50%;
    background: var(--brand-red);
  }
  .brand-name__text {
    display: flex;
    flex-direction: column;
    align-items: center;
    line-height: 1;
  }
  .brand-name__main {
    font-size: 56px;
    letter-spacing: 3px;
  }
  .brand-name__sub {
    font-size: 20px;
    letter-spacing: 5px;
    margin-top: 10px;
  }
  .edition {
    position: absolute;
    left: 840px;
    top: 652px;
    width: 290px;
    text-align: center;
    color: var(--white);
  }
  .edition__year {
    font-size: 86px;
    font-weight: 800;
    line-height: 1;
    letter-spacing: 1px;
  }
  .edition__season {
    margin-top: 22px;
    font-size: 35px;
    font-weight: 400;
    line-height: 1.15;
    letter-spacing: 1px;
  }
</style>
</head>
<body>
  <main class="catalogue-cover">
    <div class="cover-photo" role="img" aria-label="Bright room with sheer curtains: a nurse guides an older man through a stretching exercise beside an empty wheelchair"></div>

    <svg class="cover-shapes" width="1200" height="927" viewBox="0 0 1200 927" aria-hidden="true">
      <circle cx="190" cy="-250" r="320" fill="var(--brand-red)"/>
      <circle cx="-60" cy="-120" r="190" fill="var(--brand-red-dark)"/>
      <circle cx="650" cy="850" r="200" fill="var(--brand-red-light)"/>
      <circle cx="980" cy="720" r="235" fill="var(--brand-red)"/>
      <path d="M 760 650 A 235 235 0 0 0 760 927 L 820 927 A 200 200 0 0 0 760 650 Z" fill="var(--brand-red-dark)" opacity="0.55"/>
    </svg>

    <div class="brand-name">
      <div class="brand-name__text">
        <span class="brand-name__main">ORVENA</span>
        <span class="brand-name__sub">CARE</span>
      </div>
      <span class="brand-name__dot"></span>
    </div>

    <div class="edition">
      <p class="edition__year">2018</p>
      <p class="edition__season">WINTER<br>CATALOGUE</p>
    </div>
  </main>
</body>
</html>
```